Flyer Design Project

Painting and Maintenance
This is what I have as idea as Job description
Refresh, renew & revive your home. from painting to carpentry. Do you guys have any epic unique slogan?
As what we do Residential - Commercial Interior - ExteriorTrim & Molding installationWainscoting - Wallpaper removalCabinet refinishing Woodwork EnamelingDeck & Fence Cleaning & SealingPressure washConcrete & Paver Washing
I would like to have a note that says-Prompt professional service-Free estimates-Insured -"visit us on PalPorch"
I would like new ideas from you guys as well!
Carpentry

```html
<!DOCTYPE html>
<html lang="en">
<head>
<meta charset="utf-8">
<title>Harlow Painting &amp; Maintenance – Flyer Front and Back</title>
<link href="https://fonts.googleapis.com/css2?family=Montserrat:wght@300;400;600;700;800;900&display=swap" rel="stylesheet">
<style>
  :root{
    --red:#d3232a;
    --red-deep:#a8161c;
    --navy:#1c2233;
    --navy-light:#2e3650;
    --paper:#ecebe6;
    --ink:#2b2b2b;
    --grey:#5a5a5a;
    --yellow:#f2e85a;
    --call-yellow:#ffe11a;
    --white:#ffffff;
  }
  *{box-sizing:border-box;margin:0;padding:0}
  html,body{width:1200px;height:1200px;overflow:hidden}
  body{background:#d9d9d9;font-family:"Montserrat",sans-serif;position:relative}
  .card{position:absolute;left:60px;width:1080px;height:540px;overflow:hidden;background:var(--paper);box-shadow:0 6px 18px rgba(0,0,0,.18)}
  .card--back{top:40px}
  .card--front{top:620px}
  .card svg.bg{position:absolute;inset:0;width:100%;height:100%}
  .abs{position:absolute}

  .brand{display:flex;align-items:center;gap:10px;color:var(--ink);font-weight:800;text-transform:uppercase;line-height:1.05}
  .brand__dot{width:18px;height:18px;border-radius:50%;background:var(--ink);flex:none}
  .brand__name{font-size:30px;letter-spacing:.5px}
  .brand__sub{font-size:30px}

  .photo{position:absolute}
  .photo--painter{background:radial-gradient(ellipse at 55% 45%,#3d5fc4 0%,#d9d4c8 55%,rgba(236,235,230,0) 75%)}
  .photo--circle{border-radius:50%;border:5px solid var(--red);box-shadow:0 0 0 2px #fff}

  .tagline{font-size:19px;line-height:1.3;color:var(--grey);font-weight:400}
  .tagline strong{color:var(--red);font-weight:700}

  .call__head{font-weight:900;font-size:26px;color:var(--call-yellow);letter-spacing:.5px}
  .call__sub{font-size:20px;color:var(--white);letter-spacing:1.5px;font-weight:400}
  .call__phone{display:flex;align-items:center;gap:10px;font-size:34px;font-weight:800;color:var(--white);letter-spacing:1px}
  .call__phone svg{width:24px;height:24px}
  .web{display:flex;align-items:center;gap:12px;color:var(--white);font-size:24px;letter-spacing:.5px}
  .web svg{width:26px;height:26px}

  .headline{text-transform:uppercase;line-height:.92}
  .headline__red{color:var(--red);font-weight:900;font-size:84px}
  .headline__renew{color:var(--red);font-weight:600;font-size:78px}
  .headline__white{color:var(--white);font-weight:900;font-size:92px}
  .headline__home{color:var(--white);font-weight:300;font-size:40px;letter-spacing:14px;margin-top:6px}
  .headline__from{color:var(--red);font-weight:800;font-size:20px;margin:10px 0 0 100px}
  .headline__services{color:var(--white);font-size:20px;font-weight:600;letter-spacing:1px;margin-top:12px}
  .headline__services span{color:var(--red);font-size:14px;margin:0 8px}

  .services__title{display:inline-block;background:#fff;color:var(--ink);font-size:16px;font-weight:600;padding:3px 12px;letter-spacing:1px}
  .services__title b{color:var(--red);font-weight:900}
  .services__list{margin-top:10px;color:var(--white);font-size:19px;line-height:1.45;letter-spacing:.4px;max-width:1000px}
  .services__list i{font-style:normal;margin:0 8px}

  .note{background:var(--yellow);padding:16px 24px;text-align:center;box-shadow:2px 3px 6px rgba(0,0,0,.35);transform:rotate(-3deg);position:absolute}
  .note__line{font-size:17px;font-weight:600;color:var(--ink)}
  .note__strong{font-size:22px;font-weight:900;color:var(--red);line-height:1.05}
  .note__visit{font-size:15px;margin-top:6px;color:var(--ink);display:flex;align-items:center;justify-content:center;gap:8px}
  .note__visit b{color:var(--navy);font-weight:800}
</style>
</head>
<body>

<!-- Back side: services -->
<section class="card card--back">
  <svg class="bg" viewBox="0 0 1080 540" preserveAspectRatio="none" aria-hidden="true">
    <defs>
      <linearGradient id="navyBack" x1="0" y1="0" x2="1" y2="1">
        <stop offset="0" stop-color="#2e3650"/><stop offset="1" stop-color="#161b29"/>
      </linearGradient>
      <linearGradient id="redBack" x1="0" y1="0" x2="0" y2="1">
        <stop offset="0" stop-color="#c81e25"/><stop offset="1" stop-color="#a8161c"/>
      </linearGradient>
    </defs>
    <path d="M560 540 C560 420 620 300 760 250 L1080 210 V540 Z" fill="url(#navyBack)"/>
    <path d="M0 120 C250 160 520 250 1080 250 V0 H0 Z" fill="#555"/>
    <path d="M0 110 C250 150 520 236 1080 238 V0 H0 Z" fill="url(#redBack)"/>
  </svg>

  <div class="abs" style="left:30px;top:18px">
    <div class="services__title">WHAT <b>WE DO</b></div>
    <p class="services__list">★ Residential <i>★</i> Commercial Interior <i>★</i> Exterior Trim &amp; Molding installation <i>★</i> Wainscoting <i>★</i> Wallpaper Removal <i>★</i> Cabinet Refinishing <i>★</i> Woodwork Enameling <i>★</i> Deck &amp; Fence Cleaning &amp; Sealing <i>★</i> Pressure Wash <i>★</i> Concrete &amp; Paver Washing</p>
  </div>

  <div class="photo photo--circle" role="img" aria-label="Paint brush on wooden trim" style="left:150px;top:150px;width:130px;height:130px;background:radial-gradient(circle,#c9a06a,#8a5a2e)"></div>
  <div class="photo photo--circle" role="img" aria-label="Carpentry tools on timber" style="left:320px;top:185px;width:130px;height:130px;background:radial-gradient(circle,#9c7a5a,#4a3a2c)"></div>
  <div class="photo photo--circle" role="img" aria-label="Freshly sealed wooden deck" style="left:490px;top:215px;width:130px;height:130px;background:radial-gradient(circle,#b0683a,#6b3a1e)"></div>

  <div class="brand abs" style="left:30px;top:320px">
    <span class="brand__dot"></span>
    <span><span class="brand__name">Harlow Painting</span><br><span style="font-size:15px">&amp; Maintenance LLC.</span></span>
  </div>

  <div class="photo photo--painter" role="img" aria-label="Painter on a ladder rolling paint onto a wall" style="left:280px;top:330px;width:380px;height:210px"></div>

  <div class="note" style="left:760px;top:270px">
    <div class="note__line">Prompt Professional Service</div>
    <div class="note__strong">Free Estimates</div>
    <div class="note__strong">Insured</div>
    <div class="note__visit">visit us on <b>PalPorch</b></div>
  </div>

  <div class="abs" style="left:700px;top:415px">
    <div class="call__head">CALL DALE NOW</div>
    <div class="call__sub">FOR FREE QUOTATION ▶</div>
    <div class="call__phone"><svg viewBox="0 0 24 24"><circle cx="12" cy="12" r="11" fill="#fff"/><path d="M8 6l3 3-1.5 1.5a8 8 0 004 4L15 13l3 3-2 2C10 18 6 14 6 8z" fill="#1c2233"/></svg>0198 765 432</div>
    <div class="web" style="font-size:19px;margin-top:4px"><svg viewBox="0 0 24 24"><rect x="3" y="5" width="18" height="12" rx="2" fill="none" stroke="#fff" stroke-width="2"/><path d="M2 19h20" stroke="#fff" stroke-width="2"/></svg>www.harlowhomecare.com</div>
  </div>
</section>

<!-- Front side: headline -->
<section class="card card--front">
  <svg class="bg" viewBox="0 0 1080 540" preserveAspectRatio="none" aria-hidden="true">
    <defs>
      <linearGradient id="navyFront" x1="0" y1="0" x2="1" y2="1">
        <stop offset="0" stop-color="#2e3650"/><stop offset="1" stop-color="#161b29"/>
      </linearGradient>
      <linearGradient id="redFront" x1="0" y1="0" x2="1" y2="0">
        <stop offset="0" stop-color="#c81e25"/><stop offset="1" stop-color="#e0282f"/>
      </linearGradient>
    </defs>
    <path d="M560 0 H1080 V540 H420 C470 420 420 300 500 180 C540 110 520 60 560 0 Z" fill="url(#navyFront)"/>
    <path d="M0 215 C260 250 480 430 1080 452 V540 H0 Z" fill="#555"/>
    <path d="M0 232 C260 268 480 446 1080 470 V540 H0 Z" fill="url(#redFront)"/>
  </svg>

  <div class="brand abs" style="left:30px;top:24px">
    <span class="brand__dot"></span>
    <span><span class="brand__name">Harlow Painting</span><br><span style="font-size:16px">&amp; Maintenance LLC.</span></span>
  </div>

  <p class="tagline abs" style="left:30px;top:110px;width:330px">We Come To You &amp; Perform <strong>Home Repairs, Carpentry Work, Cleaning, Washing, Painting</strong> and More.....</p>

  <div class="photo photo--painter" role="img" aria-label="Painter on a ladder rolling paint onto a wall" style="left:300px;top:210px;width:330px;height:280px"></div>

  <div class="abs" style="left:30px;top:285px">
    <div class="call__head">CALL DALE NOW</div>
    <div class="call__sub">FOR FREE QUOTATION ▶</div>
    <div class="call__phone"><svg viewBox="0 0 24 24"><circle cx="12" cy="12" r="11" fill="#fff"/><path d="M8 6l3 3-1.5 1.5a8 8 0 004 4L15 13l3 3-2 2C10 18 6 14 6 8z" fill="#d3232a"/></svg>0198 765 432</div>
  </div>

  <div class="headline abs" style="left:620px;top:40px">
    <div class="headline__red">Refresh</div>
    <div class="headline__renew">Renew &amp;</div>
    <div class="headline__white">Revive</div>
    <div class="headline__home">Your Home</div>
    <div class="headline__from">From</div>
    <div class="headline__services">PAINTING<span>TO</span>CARPENTRY</div>
  </div>

  <div class="web abs" style="left:560px;top:492px"><svg viewBox="0 0 24 24"><circle cx="12" cy="12" r="11" fill="#fff"/><rect x="6" y="7" width="12" height="8" rx="1" fill="#d3232a"/><path d="M5 17h14" stroke="#d3232a" stroke-width="2"/></svg>www.harlowhomecare.com</div>
</section>

</body>
</html>
```